Harbor fairly.com a website to help those harmed by lending institutions

I am looking for a basic one page website that will be used to collect data from people filling out a form.
I will need certain key words to be optimized in order for the page to show up as high as possible in the search engines.

This web page is for people that have been harmed by their. Bank or lending institution due to inappropriate accounting practices or worse purposeful neglect.

Imagery should include an elderly person on the phone in distress because of over due bills.

Images of late notices
Images of threats of foreclosure.

** This site is to help people that are being unfairly treated even though they have made all their payments on time and the bank is commiting gross negligence.***

Some basic notes to start:

The color scheme should be similar to this site:

https://www.plovermark.example/

Here are some basic notes.

There will be more to follow.

There will need to be a collection form that people can link to and share their story.

Have you or someone you loved been hurt by their financial lending institution?

Have they/ you made all your payments on time only to constantly receive late notice penalties and additional accrued interest ?
Has your credit and good name been tarnished because your banks negligent or purposeful mis-handling of your account has caused the credit bureaus to drop your credit score?
Do you spend hours each month calling your bank to have them clear up their accounting mistakes?
Have you received threatening foreclosure notices even though you've made every payment on time ?

Well if so, you are not alone! This practise or gross incompetence is happening to many others just like you.

Your mortgage, student loan out other debt may have been sold to a new company that simply keeps losing the payments and you have to constantly clear you their errors on your time over and over again.

Budget is flexible based on design.

```html
<!DOCTYPE html>
<html lang="en">
<head>
<meta charset="utf-8">
<title>Harbor Fairly – Help for people harmed by lending institutions</title>
<link href="https://fonts.googleapis.com/css2?family=Open+Sans:wght@400;600;700;800&display=swap" rel="stylesheet">
<style>
:root{
  --green:#128a5e;
  --green-dark:#0f7c54;
  --orange:#f0821e;
  --ink:#1f1f1f;
  --text:#444;
  --muted:#666;
  --light:#f3efef;
  --dark:#2e2e2e;
  --white:#fff;
}
*{box-sizing:border-box;margin:0;padding:0}
html,body{width:1200px;height:3689px;overflow:hidden}
body{font-family:"Open Sans",sans-serif;color:var(--text);background:var(--white);position:relative}
.abs{position:absolute}
.btn{display:inline-block;background:var(--green);color:var(--white);font-weight:700;text-transform:uppercase;letter-spacing:.3px}
.photo{position:absolute}

/* header */
.site-header{position:absolute;top:0;left:0;width:1200px;height:96px;background:var(--white)}
.brand{position:absolute;left:130px;top:28px;font-size:30px;font-weight:800;color:var(--green);letter-spacing:.5px}
.main-nav{position:absolute;left:386px;top:38px;display:flex;gap:32px;font-size:14px;font-weight:600;color:var(--ink);text-transform:uppercase}
.main-nav .active{color:var(--orange)}
.call{position:absolute;left:876px;top:28px;display:flex;align-items:center;gap:12px}
.call small{display:block;font-size:11px;font-weight:700;color:var(--ink)}
.call strong{display:block;font-size:23px;font-weight:800;color:var(--green);line-height:1.05}

/* hero */
.hero{position:absolute;top:96px;left:0;width:1200px;height:516px;background:linear-gradient(90deg,#e9e6e2 0%,#ddd6cf 45%,#cfc6c3 70%,#e6e0dc 100%)}
.hero-form{position:absolute;left:145px;top:17px;width:374px;height:483px;background:rgba(40,40,40,.93);padding:32px 38px}
.hero-form h1{color:var(--white);font-size:18px;font-weight:700;line-height:1.3;margin-bottom:18px}
.field{background:var(--white);height:38px;margin-bottom:12px;font-size:11px;font-weight:700;color:var(--ink);padding:11px 12px}
.field.tall{height:110px}
.submit{display:block;background:var(--orange);color:var(--white);font-weight:800;font-size:20px;text-align:center;height:48px;line-height:48px}

/* services */
.services{position:absolute;top:612px;left:0;width:1200px;height:826px;background:var(--light)}
.section-title{position:absolute;left:0;width:1200px;text-align:center;font-size:38px;font-weight:800;color:var(--ink)}
.rule{position:absolute;left:575px;width:50px;height:3px;background:#999}
.service-card{position:absolute;width:445px;height:281px;background:var(--white);box-shadow:0 2px 6px rgba(0,0,0,.08)}
.service-card .photo{left:0;top:0;width:231px;height:281px}
.service-card h3{position:absolute;left:266px;top:32px;font-size:18px;font-weight:800;color:var(--ink);line-height:1.25;text-transform:uppercase}
.service-card p{position:absolute;left:266px;top:90px;width:150px;font-size:12px;line-height:1.5;color:var(--text)}
.service-card .btn{position:absolute;left:266px;top:217px;font-size:11px;padding:6px 10px}

/* welcome */
.welcome{position:absolute;top:1438px;left:0;width:1200px;height:598px;background:var(--white)}
.welcome .photo{left:145px;top:45px;width:453px;height:499px}
.welcome h4{position:absolute;left:652px;top:90px;font-size:22px;font-weight:800;color:var(--ink)}
.welcome h2{position:absolute;left:650px;top:112px;font-size:52px;font-weight:800;color:var(--ink);letter-spacing:.5px}
.welcome .rule{left:655px;top:186px}
.welcome p{position:absolute;left:652px;top:222px;width:400px;font-size:14.5px;line-height:1.55;color:var(--text)}
.welcome .btn{position:absolute;left:656px;top:460px;font-size:16px;padding:9px 20px}

/* blog */
.blog{position:absolute;top:2036px;left:0;width:1200px;height:674px;background:#f1f1f1}
.post{position:absolute;top:170px;width:291px;height:445px;background:var(--white);box-shadow:0 2px 6px rgba(0,0,0,.08)}
.post .photo{left:0;top:0;width:291px;height:243px}
.post h3{position:absolute;left:32px;top:267px;width:240px;font-size:16px;font-weight:800;color:var(--ink);line-height:1.25}
.post p{position:absolute;left:32px;top:320px;width:240px;font-size:12.5px;line-height:1.4}
.post .btn{position:absolute;left:32px;top:386px;font-size:11px;padding:6px 12px}

/* contact */
.contact{position:absolute;top:2710px;left:0;width:1200px;height:615px;background:linear-gradient(100deg,#262626,#3a3a3a 60%,#2c2c2c)}
.contact h2{position:absolute;left:145px;top:118px;font-size:38px;font-weight:800;color:var(--white)}
.contact .lead{position:absolute;left:145px;top:184px;width:340px;font-size:15px;font-weight:700;color:var(--white);line-height:1.45}
.info{position:absolute;left:150px;display:flex;align-items:center;gap:20px;color:var(--white);font-size:16px;line-height:1.35}
.info b{display:block;font-size:13px;font-weight:700}
.dot{width:36px;height:36px;border-radius:50%;background:var(--green);display:flex;align-items:center;justify-content:center;flex:none}
.contact-form{position:absolute;left:605px;top:69px;width:450px;height:491px;background:#c9c9c9;padding:38px 36px}
.contact-form .field{height:40px;margin-bottom:11px;border:1px solid #bbb}
.contact-form .field.tall{height:152px}
.contact-form .submit{width:150px;height:48px;line-height:48px;font-size:20px;margin-top:20px}

/* footer */
.site-footer{position:absolute;top:3325px;left:0;width:1200px;height:364px;background:var(--green)}
.site-footer .brand{position:static;display:block;text-align:center;color:var(--white);font-size:34px;padding-top:74px}
.foot-nav{text-align:center;color:var(--white);font-size:13px;margin-top:18px;word-spacing:4px}
.follow{display:flex;justify-content:center;align-items:center;gap:14px;margin-top:30px;color:var(--white);font-size:13px;font-weight:700}
.social{width:38px;height:38px;border-radius:50%}
.foot-line{position:absolute;left:145px;top:265px;width:910px;height:1px;background:rgba(255,255,255,.25)}
.copyright{position:absolute;left:0;top:299px;width:1200px;text-align:center;font-size:12px;color:var(--white)}
</style>
</head>
<body>

<header class="site-header">
  <div class="brand">HARBOR FAIRLY</div>
  <nav class="main-nav"><span class="active">Home</span><span>About Us</span><span>Services</span><span>Blog</span><span>Contact Us</span></nav>
  <div class="call">
    <svg width="30" height="30" viewBox="0 0 24 24"><path d="M6.6 10.8a15 15 0 0 0 6.6 6.6l2.2-2.2a1 1 0 0 1 1-.25 11.4 11.4 0 0 0 3.6.6 1 1 0 0 1 1 1V20a1 1 0 0 1-1 1A17 17 0 0 1 3 4a1 1 0 0 1 1-1h3.5a1 1 0 0 1 1 1c0 1.25.2 2.45.6 3.6a1 1 0 0 1-.25 1z" fill="none" stroke="#f0821e" stroke-width="1.6"/></svg>
    <div><small>CALL US NOW ON</small><strong>555.014.2290</strong></div>
  </div>
</header>

<section class="hero">
  <div class="photo" role="img" aria-label="Elderly woman on the phone looking worried at home" style="left:0;top:0;width:1200px;height:516px;background:linear-gradient(90deg,#e8e5e1 0%,#dcd5ce 50%,#e6cfd6 72%,#ece6e2 100%)"></div>
  <form class="hero-form">
    <h1>Have you or someone you loved been hurt by their financial lending institution?</h1>
    <div class="field">NAME</div>
    <div class="field">E MAIL</div>
    <div class="field">PHONE</div>
    <div class="field tall">MESSAGE</div>
    <span class="submit">SUBMIT</span>
  </form>
</section>

<section class="services">
  <h2 class="section-title" style="top:56px">OUR SERVICES</h2>
  <div class="rule" style="top:117px"></div>

  <article class="service-card" style="left:143px;top:172px">
    <div class="photo" role="img" aria-label="House at dusk" style="background:linear-gradient(180deg,#2c4f8f 0%,#3f6fb5 45%,#5b4a3a 75%,#2d2a22 100%)"></div>
    <h3>Home<br>Borrowing</h3>
    <p>Lorem ipsum dolor sit amet, consectetur adipiscing elit, sed do eiusmod tempor incididunt ut labore et dolore magna</p>
    <span class="btn">Read More</span>
  </article>
  <article class="service-card" style="left:612px;top:172px">
    <div class="photo" role="img" aria-label="Close-up of a credit card chip" style="background:linear-gradient(135deg,#c9c9c9 0%,#d24a2e 45%,#e06a3c 70%,#b8b8b8 100%)"></div>
    <h3>Credit<br>Cards</h3>
    <p>Lorem ipsum dolor sit amet, consectetur adipiscing elit, sed do eiusmod tempor incididunt ut labore et dolore magna</p>
    <span class="btn">Read More</span>
  </article>
  <article class="service-card" style="left:143px;top:477px">
    <div class="photo" role="img" aria-label="Parent lifting a child toward the sky" style="background:linear-gradient(180deg,#6f8fb0 0%,#a7bccd 60%,#7d7066 100%)"></div>
    <h3>Personal<br>Loans</h3>
    <p>Lorem ipsum dolor sit amet, consectetur adipiscing elit, sed do eiusmod tempor incididunt ut labore et dolore magna</p>
    <span class="btn">Read More</span>
  </article>
  <article class="service-card" style="left:612px;top:477px">
    <div class="photo" role="img" aria-label="Smiling couple in a new car" style="background:linear-gradient(160deg,#3a3a3a 0%,#8a7a6a 45%,#c9b49c 70%,#4a4a4a 100%)"></div>
    <h3>Auto<br>Finance</h3>
    <p>Lorem ipsum dolor sit amet, consectetur adipiscing elit, sed do eiusmod tempor incididunt ut labore et dolore magna</p>
    <span class="btn">Read More</span>
  </article>
</section>

<section class="welcome">
  <div class="photo" role="img" aria-label="Hands reviewing paperwork beside a laptop" style="background:linear-gradient(135deg,#d9d6d2 0%,#ecebe8 45%,#c9b9a6 80%,#b8a38c 100%)"></div>
  <h4>WELCOME TO</h4>
  <h2>HARBOR FAIRLY</h2>
  <div class="rule"></div>
  <p>At vero eos et accusamus et iusto odio dignissimos ducimus qui blanditiis praesentium voluptatum deleniti atque corrupti quos dolores et quas molestias excepturi sint occaecati cupiditate non provident, similique sunt in culpa qui officia deserunt mollitia animi, id est laborum et dolorum fuga. Et harum quidem rerum facilis est et expedita distinctio. Nam libero tempore, cum soluta nobis est eligendi optio cumque nihil impedit quo minus id quod.</p>
  <span class="btn">Read More</span>
</section>

<section class="blog">
  <h2 class="section-title" style="top:60px">LATEST BLOG</h2>
  <div class="rule" style="top:121px"></div>

  <article class="post" style="left:133px">
    <div class="photo" role="img" aria-label="Business meeting over documents and a laptop" style="background:linear-gradient(135deg,#5a4634 0%,#8a6a4c 45%,#d8d4cf 75%,#3a3a3a 100%)"></div>
    <h3>Lorem Ipsum is simply dummy text of the printing</h3>
    <p>There are many variations of passages of Lorem Ipsum available, but the majority have suffered.</p>
    <span class="btn">Read More</span>
  </article>
  <article class="post" style="left:452px">
    <div class="photo" role="img" aria-label="Handshake across a desk with papers" style="background:linear-gradient(135deg,#6a5440 0%,#9a7a5a 40%,#dcd8d2 70%,#2f2f2f 100%)"></div>
    <h3>Lorem Ipsum is simply dummy text of the printing</h3>
    <p>There are many variations of passages of Lorem Ipsum available, but the majority have suffered.</p>
    <span class="btn">Read More</span>
  </article>
  <article class="post" style="left:772px">
    <div class="photo" role="img" aria-label="Desk with phone, charts and a laptop seen from above" style="background:linear-gradient(135deg,#f0f0ef 0%,#e2e2e0 50%,#b9b9b9 80%,#8e8e8e 100%)"></div>
    <h3>Lorem Ipsum is simply dummy text of the printing</h3>
    <p>There are many variations of passages of Lorem Ipsum available, but the majority have suffered.</p>
    <span class="btn">Read More</span>
  </article>
</section>

<section class="contact">
  <h2>CONTACT US</h2>
  <p class="lead">At vero eos et accusamus et iusto odio dignissimos ducimus qui blanditiis.</p>

  <div class="info" style="top:294px">
    <span class="dot"><svg width="16" height="16" viewBox="0 0 24 24"><path d="M12 2a7 7 0 0 0-7 7c0 5 7 13 7 13s7-8 7-13a7 7 0 0 0-7-7zm0 9.5A2.5 2.5 0 1 1 12 6.5a2.5 2.5 0 0 1 0 5z" fill="#fff"/></svg></span>
    <span>1180 Willow Crest Lane<br>Marlow Springs, KY 40999</span>
  </div>
  <div class="info" style="top:372px">
    <span class="dot"><svg width="15" height="15" viewBox="0 0 24 24"><path d="M6.6 10.8a15 15 0 0 0 6.6 6.6l2.2-2.2a1 1 0 0 1 1-.25 11.4 11.4 0 0 0 3.6.6 1 1 0 0 1 1 1V20a1 1 0 0 1-1 1A17 17 0 0 1 3 4a1 1 0 0 1 1-1h3.5a1 1 0 0 1 1 1c0 1.25.2 2.45.6 3.6a1 1 0 0 1-.25 1z" fill="#fff"/></svg></span>
    <span><b>CALL US</b>555.010.4477</span>
  </div>
  <div class="info" style="top:452px">
    <span class="dot"><svg width="15" height="15" viewBox="0 0 24 24"><path d="M3 6h18v12H3z" fill="#fff"/><path d="M3 6l9 7 9-7" fill="none" stroke="#128a5e" stroke-width="2"/></svg></span>
    <span><b>E MAIL US</b>info@harborfairly.com</span>
  </div>

  <form class="contact-form">
    <div class="field">NAME</div>
    <div class="field">E MAIL</div>
    <div class="field">PHONE</div>
    <div class="field">SUBJECT</div>
    <div class="field tall">MESSAGE</div>
    <span class="submit">SUBMIT</span>
  </form>
</section>

<footer class="site-footer">
  <span class="brand">HARBOR FAIRLY</span>
  <nav class="foot-nav">HOME | ABOUT US | SERVICES | BLOG | CONTACT US</nav>
  <div class="follow">
    <span>FOLLOW US</span>
    <span class="social" role="img" aria-label="Social profile" style="background:#3b5ea8"></span>
    <span class="social" role="img" aria-label="Social profile" style="background:#1da1e2"></span>
    <span class="social" role="img" aria-label="Social profile" style="background:#0a2a66"></span>
  </div>
  <div class="foot-line"></div>
  <p class="copyright">Copyrights @ 2019 All Rights Reserved</p>
</footer>

</body>
</html>
```